TKA Electricial Contracting Services

Hi guys, after a design for my small electrical company, have logo design files to be incorporated into the layout, the basic concept is electrical contracting services for residential, commercial, industrial & data services, image is clean clear and strong,

Card format is to have a nice clean logo on front,with maybe the Residential – commercial – industrial - data, followed with licensed & insured, followed by contact details on backside of the card.

Target Market(s)

Residential, commercial, industrial sectors.

Industry/Entity Type

Electrical

Contact Information for Business Card

TKA logo,
Residential – commercial – industrial - data
REC: 61372
Email: tka@poralink.net.au
Phone: 0458 203 719

Requirements
Must have
• Clean & strong design.
Nice to have
• If possible, I would like the logo colours inverted so the text is orange and the background is black on the front of the card, then the backside of the card be the reverse colour
Should not have
• No Sparks, lightning bolts,

```html
<!DOCTYPE html>
<html lang="en">
<head>
<meta charset="utf-8">
<title>TKA Electrical – Business Cards</title>
<link rel="stylesheet" href="https://fonts.googleapis.com/css2?family=Open+Sans:wght@400;600;700&display=swap">
<style>
  :root {
    --stage: #b9b9b7;
    --orange: #f28128;
    --black: #050505;
    --white: #ffffff;
  }
  * { box-sizing: border-box; margin: 0; padding: 0; }
  html, body {
    width: 1200px;
    height: 900px;
    overflow: hidden;
    background: var(--stage);
    font-family: "Open Sans", Arial, sans-serif;
  }
  .canvas { position: relative; width: 1200px; height: 900px; }

  .card {
    position: absolute;
    width: 620px;
    height: 354px;
    overflow: hidden;
    box-shadow: 0 6px 18px rgba(0,0,0,0.25);
  }

  .brand { color: var(--black); font-weight: 700; line-height: 1; }
  .brand__mark { font-size: 92px; letter-spacing: 2px; display: block; }
  .brand__name { font-size: 17px; display: block; margin-top: 4px; letter-spacing: 0.5px; }

  /* Front */
  .card--front {
    left: 540px;
    top: 80px;
    display: grid;
    grid-template-rows: 18% 64% 18%;
  }
  .band--black { background: var(--black); }
  .band--orange {
    background: var(--orange);
    display: flex;
    align-items: center;
    justify-content: center;
  }
  .card--front .brand { margin-left: 60px; }

  /* Back */
  .card--back {
    left: 60px;
    top: 470px;
    background: var(--black);
  }
  .back__top {
    position: absolute;
    left: 0; top: 0;
    width: 100%; height: 130px;
    background: var(--orange);
  }
  .back__logo-block {
    position: absolute;
    left: 300px; top: 130px;
    width: 320px; height: 72px;
    background: var(--orange);
  }
  .back__bottom {
    position: absolute;
    left: 0; bottom: 0;
    width: 100%; height: 34px;
    background: var(--orange);
  }
  .card--back .brand {
    position: absolute;
    right: 40px;
    top: 70px;
  }
  .card--back .brand__mark { font-size: 84px; }
  .card--back .brand__name { font-size: 15px; }

  .person {
    position: absolute;
    left: 24px;
    top: 146px;
    color: var(--white);
  }
  .person__name { font-size: 22px; font-weight: 700; line-height: 1.2; }
  .person__role { font-size: 13px; line-height: 1.3; }

  .contacts {
    position: absolute;
    right: 26px;
    top: 212px;
    list-style: none;
    color: var(--white);
  }
  .contacts li {
    font-size: 16px;
    line-height: 21px;
    display: flex;
    justify-content: flex-end;
    align-items: center;
    gap: 10px;
    white-space: nowrap;
  }
  .contacts svg { width: 13px; height: 13px; fill: var(--white); flex: none; }
</style>
</head>
<body>
<main class="canvas">

  <section class="card card--front" aria-label="Business card front">
    <div class="band--black"></div>
    <div class="band--orange">
      <div class="brand">
        <span class="brand__mark">TKA</span>
        <span class="brand__name">Tom Kelly Electrical</span>
      </div>
    </div>
    <div class="band--black"></div>
  </section>

  <section class="card card--back" aria-label="Business card back">
    <div class="back__top"></div>
    <div class="back__logo-block"></div>
    <div class="back__bottom"></div>

    <div class="brand">
      <span class="brand__mark">TKA</span>
      <span class="brand__name">Tom Kelly Electrical</span>
    </div>

    <div class="person">
      <p class="person__name">Daniel Hartley</p>
      <p class="person__role">Managing Director</p>
    </div>

    <ul class="contacts">
      <li>123.456.7890
        <svg viewBox="0 0 16 16" aria-hidden="true"><path d="M3 2h3l1 3-2 1c1 2 2 3 4 4l1-2 3 1v3c0 1-1 2-2 2C6 14 2 10 2 4c0-1 0-2 1-2z"/></svg>
      </li>
      <li>123.456.7890
        <svg viewBox="0 0 16 16" aria-hidden="true"><path d="M4 1h8v14H4z M6 3v8h4V3z M7 12h2v2H7z" fill-rule="evenodd"/></svg>
      </li>
      <li>info@youremail.com
        <svg viewBox="0 0 16 16" aria-hidden="true"><path d="M1 3h14v10H1z M2 4l6 5 6-5v-0.1L8 8 2 4z" fill-rule="evenodd"/></svg>
      </li>
      <li>www.website.com
        <svg viewBox="0 0 16 16" aria-hidden="true"><path d="M6 10l4-4 1 1-4 4z M2 10l3-3 1 1-3 3 2 2 3-3 1 1-3 3h-1l-3-3z M8 4l3-3h1l3 3v1l-3 3-1-1 3-3-2-2-3 3z"/></svg>
      </li>
      <li>1234, Address Goes Here, Country Name, 123456
        <svg viewBox="0 0 16 16" aria-hidden="true"><path d="M8 1a5 5 0 0 1 5 5c0 4-5 9-5 9S3 10 3 6a5 5 0 0 1 5-5z M8 4a2 2 0 1 0 0 4 2 2 0 0 0 0-4z" fill-rule="evenodd"/></svg>
      </li>
    </ul>
  </section>

</main>
</body>
</html>
```